Organic Mavu (Coffee) Scrub Label for high end product

Need a product label for a coffee based body scrub called Mavu Body Scrub a 100% organic product. Our primary target is the yoga community so designs should reflect calm, perhaps incorporate eastern yoga symbology. simpler the better. Design should include both a round lid label and a rectangular wrap around label.

Target Market(s)

yoga community, people with cellulite, etc.

Industry/Entity Type

Community

```html
<!DOCTYPE html>
<html lang="en">
<head>
<meta charset="utf-8">
<title>Mavu Body Scrub – Wrap Label</title>
<link rel="stylesheet" href="https://fonts.googleapis.com/css2?family=Alegreya+Sans:ital,wght@1,700&family=Varela+Round&family=Archivo:wght@700;800&display=swap">
<style>
  :root {
    --coffee: #7b4b33;
    --steam: #bca89c;
    --ink: #1d1b1b;
    --gold: #c9a23e;
    --leaf: #3aa94a;
    --paper: #ffffff;
  }
  * { box-sizing: border-box; margin: 0; padding: 0; }
  html, body { width: 1200px; height: 1000px; overflow: hidden; background: var(--paper); }
  .label { position: relative; width: 1200px; height: 1000px; background: var(--paper); }

  .bean-scatter { position: absolute; }
  .bean-scatter--left {
    left: 15px; top: 10px; width: 220px; height: 200px;
    border-radius: 0 0 90px 30px;
    background: radial-gradient(ellipse at 40% 30%, rgba(123,75,51,.85), rgba(123,75,51,.35) 70%, rgba(123,75,51,0) 100%);
  }
  .bean-scatter--right {
    left: 560px; top: 0; width: 630px; height: 290px;
    border-radius: 0 0 40px 260px;
    background: radial-gradient(ellipse at 65% 25%, rgba(123,75,51,.85), rgba(123,75,51,.4) 65%, rgba(123,75,51,0) 100%);
  }

  .yoga-figures {
    position: absolute; left: 150px; top: 112px; width: 390px; height: 130px;
    background: linear-gradient(to top, rgba(123,75,51,.45), rgba(123,75,51,.08));
    border-radius: 120px 120px 0 0;
  }

  .story-frame { position: absolute; left: 0; top: 0; width: 1200px; height: 1000px; pointer-events: none; }

  .story {
    position: absolute; left: 97px; top: 250px; width: 423px;
    font-family: "Alegreya Sans", "Trebuchet MS", sans-serif;
    font-style: italic; font-weight: 700;
    font-size: 29px; line-height: 40px; color: var(--ink);
  }
  .story__line {
    display: block; white-space: nowrap;
    text-align: justify; text-align-last: justify;
  }
  .story__line--short { width: 266px; }
  .story__line--end { text-align-last: left; }

  .organic-seal {
    position: absolute; left: 392px; top: 756px; width: 184px; height: 184px;
    border-radius: 50%; background: var(--paper);
    border: 14px solid var(--leaf);
  }

  .steam-swirl {
    position: absolute; left: 655px; top: 215px; width: 505px; height: 575px;
    border-radius: 50%;
    background: radial-gradient(ellipse at 50% 50%, rgba(188,168,156,.75), rgba(188,168,156,.3) 60%, rgba(188,168,156,0) 78%);
  }

  .brand-name {
    position: absolute; left: 812px; top: 305px; width: 200px; text-align: center;
    font-family: "Varela Round", "Arial Rounded MT Bold", sans-serif;
    font-weight: 400; font-size: 66px; line-height: 80px; color: var(--ink);
  }

  .product-title {
    position: absolute; left: 640px; top: 410px; width: 540px;
    font-family: "Archivo", Arial, sans-serif; font-weight: 800;
    font-size: 150px; line-height: 185px; color: var(--gold);
  }
  .product-title__word { display: block; text-align: center; }
  .product-title__word--first { padding-right: 40px; }
  .product-title__word--second { padding-left: 60px; }

  .benefits {
    position: absolute; left: 615px; top: 838px; width: 555px; text-align: center;
    font-family: "Archivo", Arial, sans-serif; font-weight: 800;
    font-size: 32px; line-height: 40px; color: var(--coffee);
  }
  .benefits__dot { font-size: 22px; vertical-align: 3px; padding: 0 4px; }

  .net-weight {
    position: absolute; left: 812px; top: 954px; width: 200px; text-align: center;
    font-family: "Archivo", Arial, sans-serif; font-weight: 700;
    font-size: 20px; line-height: 28px; color: var(--ink);
  }
</style>
</head>
<body>
<main class="label">
  <div class="bean-scatter bean-scatter--left" role="img" aria-label="Scattered roasted coffee beans"></div>
  <div class="bean-scatter bean-scatter--right" role="img" aria-label="Scattered roasted coffee beans"></div>

  <div class="steam-swirl" role="img" aria-label="Soft swirl of coffee steam"></div>

  <div class="yoga-figures" role="img" aria-label="Line drawing of people in calm yoga poses"></div>

  <svg class="story-frame" viewBox="0 0 1200 1000" aria-hidden="true">
    <path d="M66 942 V243 H543 V750 M66 942 H428" fill="none" stroke="var(--coffee)" stroke-width="4"/>
  </svg>

  <div class="story">
    <span class="story__line">Lorem ipsum dolor sit amet,</span>
    <span class="story__line">consectetur adipiscing elit. Sed</span>
    <span class="story__line">at ante. Mauris eleifend, quam</span>
    <span class="story__line">a vulputate dictum, massa</span>
    <span class="story__line">quam dapibus leo, eget vulpu-</span>
    <span class="story__line">tate orci purus ut lorem. In frin-</span>
    <span class="story__line">gilla mi in ligula. Pellentesque</span>
    <span class="story__line">aliquam quam vel dolor. Nunc</span>
    <span class="story__line">adipiscing. Sed quam odio,</span>
    <span class="story__line">tempus ac, aliquam molestie,</span>
    <span class="story__line">varius ac, tellus. Vestibulum</span>
    <span class="story__line">ut nulla aliquam risus rutrum</span>
    <span class="story__line story__line--short">interdum. Pellen-</span>
    <span class="story__line story__line--short">tesque lorem. Cura-</span>
    <span class="story__line story__line--short">bitur sit amet erat</span>
    <span class="story__line story__line--short">quis risus feugiat</span>
    <span class="story__line story__line--short story__line--end">viverra.</span>
  </div>

  <div class="organic-seal" role="img" aria-label="Organic certification seal"></div>

  <p class="brand-name">Mavu</p>

  <h1 class="product-title">
    <span class="product-title__word product-title__word--first">Body</span>
    <span class="product-title__word product-title__word--second">Scrub</span>
  </h1>

  <p class="benefits">Restore elasticity<span class="benefits__dot">•</span>Super<br>hydration<span class="benefits__dot">•</span>Boost cell turnover</p>

  <p class="net-weight">3.3oz | 100g</p>
</main>
</body>
</html>
```